Looking to design a new sign for our church.

Looking for a new sign
4 x 8 feet dimension
We are renaming the church "Medlow Ridge Community Church"
looking for legible graphics
Would like some type of backdrop being a family tree (oak) / open to other ideas as you are led
I have included a pic of the old sign for your review
would like to incorporate our ministry logo on the lower right hand corner of the sign / see file attached

```html
<!DOCTYPE html>
<html lang="en">
<head>
<meta charset="utf-8">
<title>Medlow Ridge Community Church – Sign</title>
<link href="https://fonts.googleapis.com/css2?family=Bebas+Neue&family=Montserrat:wght@800&display=swap" rel="stylesheet">
<style>
  :root {
    --navy: #004a6b;
    --teal: #00728f;
    --sun-yellow: #fec820;
    --pale-yellow: #ffe48a;
    --cream: #fff8e8;
    --white: #ffffff;
    --backdrop: #ececec;
    --cloth-light: #f2b27a;
    --cloth-dark: #c4622a;
  }
  * { margin: 0; padding: 0; box-sizing: border-box; }
  html, body {
    width: 858px;
    height: 1200px;
    overflow: hidden;
    background: var(--backdrop);
  }
  .sign {
    position: absolute;
    left: 0;
    top: 385px;
    width: 858px;
    height: 429px;
    overflow: hidden;
    background: linear-gradient(100deg, var(--sun-yellow) 0%, var(--pale-yellow) 45%, var(--cream) 100%);
  }
  .name-top {
    position: absolute;
    left: 50px;
    top: 39px;
    height: 68px;
    padding: 0 12px 0 11px;
    background: var(--white);
    color: var(--navy);
    font-family: "Bebas Neue", sans-serif;
    font-size: 79px;
    line-height: 76px;
    letter-spacing: 0.5px;
    white-space: nowrap;
  }
  .name-rule {
    position: absolute;
    left: 50px;
    top: 116px;
    width: 3px;
    height: 181px;
    background: var(--navy);
  }
  .name-main {
    position: absolute;
    left: 61px;
    color: var(--navy);
    font-family: "Bebas Neue", sans-serif;
    font-size: 126px;
    line-height: 1;
    white-space: nowrap;
  }
  .name-main.line-one { top: 110px; }
  .name-main.line-two { top: 205px; }
  .services {
    position: absolute;
    left: 50px;
    top: 330px;
    display: flex;
    align-items: stretch;
    color: var(--navy);
    font-family: "Montserrat", sans-serif;
    font-weight: 800;
    font-size: 22.5px;
    line-height: 0.98;
    letter-spacing: 0.3px;
  }
  .service {
    padding-right: 9px;
  }
  .service + .service {
    border-left: 2px solid var(--navy);
    padding-left: 8px;
  }
  .hill {
    position: absolute;
    left: 0;
    top: 0;
    width: 858px;
    height: 429px;
  }
  .cross-illustration {
    position: absolute;
    left: 563px;
    top: 64px;
    width: 229px;
    height: 262px;
    border-radius: 6px;
    background: linear-gradient(160deg, var(--cloth-light) 0%, var(--cloth-dark) 45%, var(--teal) 100%);
  }
  .ministry-name {
    position: absolute;
    left: 790px;
    top: 290px;
    width: 64px;
    color: var(--navy);
    font-family: "Montserrat", sans-serif;
    font-weight: 800;
    font-size: 8px;
    line-height: 1.15;
    text-align: center;
  }
</style>
</head>
<body>
  <main class="sign">
    <svg class="hill" viewBox="0 0 858 429" aria-hidden="true">
      <path d="M389 429 C 520 372, 640 330, 727 322 C 780 318, 825 330, 858 343 L 858 429 Z" fill="var(--teal)"/>
    </svg>

    <div class="name-top">MEDLOW RIDGE</div>
    <div class="name-rule"></div>
    <div class="name-main line-one">COMMUNITY</div>
    <div class="name-main line-two">CHURCH</div>

    <div class="services">
      <div class="service">WORSHIP<br>SERVICE</div>
      <div class="service">SUNDAY<br>SCHOOL</div>
      <div class="service">WEDNESDAY<br>SERVICE</div>
    </div>

    <div class="cross-illustration" role="img" aria-label="Illustration of a cross draped with flowing orange cloth standing on the hilltop, with sun rays behind"></div>

    <div class="ministry-name">Ridgeline Ministries</div>
  </main>
</body>
</html>
```